Window Cleaning Flyer targeting Shopfronts and Small Commercial Work

Single page flyer similar to the flyer targeting small commercial work and shopfronts

Please include the following text:

Brisk Pane Services delivers high quality service to suburbs all around Melbourne. From Frankston to Kalkallo, Brisk has you covered!

With over 10 years experience, Brisk specialises in providing:
- Window Cleaning: via elevated work platforms, rope access and extension poles
- Pressure Cleaning: Including chlorine treatment to prevent mould regrowth on concrete area
- Roof Gutter Cleaning: using our ladder free gutter vacuum

We pride ourselves on neat and professional presentation and vast geographical reach across Melbourne.

Our services can be completed on a frequency that meets your window cleaning needs. Whether a weekly clean or a yearly service.

Brisk Pane Services Melbourne takes care of all your window cleaning needs.

Contact Us now for free quote!

Target Market(s)

Small business and commercial building owners

Industry/Entity Type

Window Cleaning

Requirements
Must have
• Only use photos/logos provided
Should not have
• Stock phots

```html
<!DOCTYPE html>
<html lang="en">
<head>
<meta charset="utf-8">
<title>Brisk Pane Services – Flyer</title>
<link href="https://fonts.googleapis.com/css2?family=Noto+Sans:wght@700&display=swap" rel="stylesheet">
<style>
  :root {
    --navy-top: #1d4282;
    --navy-mid: #14305e;
    --navy-deep: #0b1424;
    --accent: #f7f01a;
    --ink: #ffffff;
  }
  * { margin: 0; padding: 0; box-sizing: border-box; }
  html, body { width: 927px; height: 1200px; overflow: hidden; background: var(--navy-deep); }
  .flyer {
    position: relative; width: 927px; height: 1200px; overflow: hidden;
    font-family: "Noto Sans", Verdana, sans-serif; font-weight: 700; color: var(--ink);
  }
  .flyer-art { position: absolute; inset: 0; }
  .hl { color: var(--accent); }
  .brand {
    position: absolute; left: 32px; top: 22px;
    color: var(--accent); font-size: 50px; line-height: 56px; letter-spacing: 1px;
  }
  .coverage {
    position: absolute; right: 22px; top: 52px; text-align: right;
    font-size: 21px; line-height: 32px; letter-spacing: 1.4px; white-space: nowrap;
  }
  .tagline {
    position: absolute; left: 9px; top: 158px;
    font-size: 23px; letter-spacing: 1.8px; white-space: nowrap;
  }
  .intro {
    position: absolute; left: 437px; top: 232px;
    font-size: 27px; line-height: 38px; letter-spacing: 2px; white-space: nowrap;
  }
  .service-list { position: absolute; left: 520px; top: 331px; list-style: none; }
  .service-name { color: var(--accent); font-size: 24px; letter-spacing: 1.8px; line-height: 37px; white-space: nowrap; }
  .service-detail { font-size: 16px; letter-spacing: 1.3px; line-height: 38px; white-space: nowrap; }
  .pride {
    position: absolute; left: 0; top: 678px; width: 927px; text-align: center;
    font-size: 26px; line-height: 38px; letter-spacing: 1.5px; white-space: nowrap;
  }
  .frequency {
    position: absolute; left: 22px; top: 858px;
    font-size: 29px; line-height: 38px; letter-spacing: 1.5px; white-space: nowrap;
  }
  .promise {
    position: absolute; right: 14px; top: 1110px;
    font-size: 16px; line-height: 22px; letter-spacing: 1px; white-space: nowrap;
  }
  .cta {
    position: absolute; right: 12px; top: 1146px;
    color: var(--accent); font-size: 35px; letter-spacing: 2.4px; white-space: nowrap;
  }
</style>
</head>
<body>
<main class="flyer">
  <svg class="flyer-art" width="927" height="1200" viewBox="0 0 927 1200">
    <defs>
      <linearGradient id="bg" x1="0" y1="0" x2="0.6" y2="1">
        <stop offset="0" stop-color="#1d4282"/>
        <stop offset="0.5" stop-color="#14305e"/>
        <stop offset="1" stop-color="#0b1424"/>
      </linearGradient>
      <linearGradient id="facade" x1="0" y1="0" x2="0" y2="1">
        <stop offset="0" stop-color="#9a8468"/>
        <stop offset="0.7" stop-color="#7c6e5a"/>
        <stop offset="1" stop-color="#4f6a3a"/>
      </linearGradient>
      <linearGradient id="brick" x1="0" y1="0" x2="1" y2="0">
        <stop offset="0" stop-color="#8a4a34"/>
        <stop offset="0.6" stop-color="#3a3a3a"/>
        <stop offset="1" stop-color="#5b7a3c"/>
      </linearGradient>
    </defs>
    <rect class="backdrop" width="927" height="1200" fill="url(#bg)"/>
    <polygon class="band" points="0,200 927,210 927,216 0,232" fill="#f7f01a"/>
    <polygon class="photo" role="img" aria-label="Photo of a cleaner washing windows of a timber-slatted building with an extension pole"
      points="0,234 404,228 472,644 0,652" fill="url(#facade)"/>
    <polygon class="band" points="404,228 414,228 512,640 472,644" fill="#f7f01a"/>
    <polygon class="band" points="0,652 927,636 927,664 0,664" fill="#f7f01a"/>
    <polygon class="band" points="0,774 927,832 927,840 0,800" fill="#f7f01a"/>
    <polygon class="photo" role="img" aria-label="Photo of a cleaner on an elevated work platform cleaning windows of a brick building"
      points="620,829 927,839 927,1050 606,1054" fill="url(#brick)"/>
    <polygon class="band" points="610,828 620,829 606,1054 596,1054" fill="#f7f01a"/>
    <polygon class="band" points="0,1100 927,1044 927,1064 0,1116" fill="#f7f01a"/>
  </svg>

  <div class="brand">Brisk Pane<br>Services</div>

  <p class="coverage">From <span class="hl">FRANKSTON</span> to <span class="hl">KALKALLO</span>,<br>Brisk has you covered!</p>

  <p class="tagline">delivers <span class="hl">HIGH QUALITY</span> service to suburbs all around <span class="hl">MELBOURNE.</span></p>

  <p class="intro">With over 10 years experience,<br>Brisk specialises in providing:</p>

  <ul class="service-list">
    <li>
      <div class="service-name">- Window Cleaning:</div>
      <div class="service-detail">via elevated work platforms,</div>
      <div class="service-detail">rope access and extension poles</div>
    </li>
    <li>
      <div class="service-name">- Pressure Cleaning:</div>
      <div class="service-detail">&nbsp;Including chlorine treatment to prevent</div>
      <div class="service-detail">mould regrowth on concrete area</div>
    </li>
    <li>
      <div class="service-name">- Roof Gutter Cleaning:</div>
      <div class="service-detail">using our ladder free gutter vacuum</div>
    </li>
  </ul>

  <p class="pride">We <span class="hl">PRIDE</span> ourselves on <span class="hl">NEAT</span> and <span class="hl">PROFESSIONAL</span> presentation<br>and vast <span class="hl">GEOGRAPHICAL</span> reach across <span class="hl">MELBOURNE.</span></p>

  <p class="frequency">Our <span class="hl">SERVICES</span> can be <span class="hl">COMPLETED</span><br>on a <span class="hl">FREQUENCY</span> that meets <span class="hl">YOUR</span><br>window cleaning <span class="hl">NEEDS</span>. Whether a<br><span class="hl">WEEKLY</span> clean or a <span class="hl">YEARLY</span> service.</p>

  <p class="promise">Brisk Pane Services Melbourne takes care of all your window cleaning needs.</p>

  <p class="cta">CONTACT US NOW FOR A FREE QUOTE!</p>
</main>
</body>
</html>
```